pine ridge heating & air company flyer for tradeboard ad

size should be 1200x900
this is an ac company, we have a logo but not necessary to use
we offer free estimates, we are open 24/7, fast and affordable
service, licensed and insured
we sell all brands and service all
we offer services for refrigeration residential and commercial
I will post a few of my ads I made but need a pros idea

Pine Ridge Heating & Air Company
407-315-8842
pineridgeair@mailbox-example.com
pineridgeair247.example
license # must be on flyer state law it is CAC5327164
if you use the logo please remove the building

Target Market(s)

any one who needs has an ac in home

Industry/Entity Type

Hvac

Requirements
Must have
• contact info must be big

```html
<!DOCTYPE html>
<html lang="en">
<head>
<meta charset="utf-8">
<title>Pine Ridge Heating &amp; Air Company</title>
<link rel="stylesheet" href="https://fonts.googleapis.com/css2?family=Arimo:ital,wght@0,400;0,700;1,700&display=swap">
<style>
:root{
  --navy:#0b1a78;
  --deep:#07123f;
  --red:#d0141c;
  --white:#ffffff;
  --band:#050c2e;
  --chip:#8fa2c9;
  --brand-text:#b9c6e6;
}
*{margin:0;padding:0;box-sizing:border-box}
html,body{width:1200px;height:900px;overflow:hidden;background:var(--white)}
.flyer{position:relative;width:1200px;height:900px;overflow:hidden;font-family:"Arimo",Arial,sans-serif}
.backdrop{position:absolute;inset:0}
.license{position:absolute;top:9px;right:14px;color:var(--white);font-weight:700;font-size:14px;letter-spacing:.3px}
.brand-name{position:absolute;left:90px;top:110px;width:420px;text-align:center;color:var(--red);font-weight:700;font-size:46px;line-height:1.1}
.services-title{position:absolute;left:748px;top:66px;color:var(--navy);font-weight:700;font-size:39px;line-height:66px;letter-spacing:3px}
.brands{position:absolute;left:588px;top:258px;width:612px;height:157px;background:var(--band);padding:20px 10px 0 12px;color:var(--white)}
.brands h2{font-weight:400;font-size:26px;letter-spacing:-.3px;margin-bottom:16px}
.brand-row{display:flex;align-items:center;justify-content:space-between;height:36px;font-size:13px;font-weight:700;font-style:italic}
.brand-row .dot{width:4px;height:4px;border-radius:50%;background:var(--white)}
.brand-row .chip{width:16px;height:22px;background:var(--chip);border-radius:3px}
.brand-row b{color:var(--brand-text)}
.estimates{position:absolute;left:0;top:415px;width:590px;height:86px;background:var(--band);color:var(--white);font-weight:700;font-size:46px;text-align:center;line-height:86px;letter-spacing:.5px}
.phone{position:absolute;left:34px;top:515px;color:var(--navy);font-weight:700;font-size:76px;letter-spacing:5px;text-shadow:0 0 14px rgba(255,255,255,.55)}
.web{position:absolute;left:32px;top:625px;color:var(--white);font-weight:700;font-size:40px;letter-spacing:-.3px}
.email{position:absolute;left:70px;top:698px;color:var(--deep);font-weight:400;font-size:28px}
.promise{position:absolute;left:0;top:770px;width:800px;height:110px;background:linear-gradient(90deg,var(--white) 0%,var(--white) 60%,rgba(255,255,255,0) 100%);padding-left:34px}
.promise .hours{color:var(--red);font-weight:700;font-style:italic;font-size:46px;line-height:52px}
.promise .tagline{color:var(--deep);font-weight:700;font-style:italic;font-size:46px;line-height:50px;letter-spacing:0}
.credentials{position:absolute;left:820px;top:467px;width:140px;text-align:center;color:var(--deep);font-weight:700;font-size:24px;line-height:31px;letter-spacing:.5px}
.equipment{position:absolute;left:770px;top:455px;width:430px;height:445px}
</style>
</head>
<body>
<main class="flyer">
  <svg class="backdrop" width="1200" height="900" viewBox="0 0 1200 900" aria-hidden="true">
    <defs>
      <radialGradient id="leftGlow" cx="0.3" cy="0.35" r="0.8">
        <stop offset="0" stop-color="#4a8bff"/>
        <stop offset="0.55" stop-color="#1b55e6"/>
        <stop offset="1" stop-color="#0a2aa8"/>
      </radialGradient>
      <linearGradient id="topRight" x1="0" y1="0" x2="1" y2="1">
        <stop offset="0" stop-color="#6f9df6"/>
        <stop offset="1" stop-color="#8fb4fa"/>
      </linearGradient>
      <linearGradient id="lowRight" x1="0" y1="0" x2="0" y2="1">
        <stop offset="0" stop-color="#c6d8f8"/>
        <stop offset="1" stop-color="#9fbcf2"/>
      </linearGradient>
    </defs>
    <rect width="1200" height="900" fill="url(#leftGlow)"/>
    <path d="M700 0 Q600 180 578 415 L1200 415 L1200 0 Z" fill="#ffffff"/>
    <path d="M712 0 Q614 180 592 415 L1200 415 L1200 0 Z" fill="url(#topRight)"/>
    <path d="M578 415 Q585 640 780 900 L1200 900 L1200 415 Z" fill="url(#lowRight)"/>
  </svg>

  <div class="license">LICENSE #CAC5327164</div>

  <h1 class="brand-name">Pine Ridge<br>Heating &amp; Air<br>Company</h1>

  <p class="services-title">Residential and<br>Commercial</p>

  <section class="brands">
    <h2>We repair and service these brands + more,</h2>
    <div class="brand-row">
      <b>TRALON</b><span class="dot"></span><b>Corvane</b><span class="dot"></span><b>Brimley</b><span class="dot"></span><b>Avelo</b><span class="dot"></span><b>Warmhaven</b><span class="dot"></span><b>Ressa</b><span class="dot"></span><b>ROAN</b>
    </div>
    <div class="brand-row">
      <b>YARROW</b><span class="dot"></span><b>TEMPO AIR</b><span class="dot"></span><span class="chip"></span><span class="dot"></span><b>Amberline</b><span class="dot"></span><b>Goodwell</b><span class="dot"></span><b>Colbrook</b><span class="dot"></span><b>DUNMORE</b>
    </div>
  </section>

  <div class="estimates">FREE ESTIMATES</div>
  <div class="phone">407-315-8842</div>
  <div class="web">www.pineridgeair247.example</div>
  <div class="email">pineridgeair@mailbox-example.com</div>

  <div class="promise">
    <div class="hours">24/7</div>
    <div class="tagline">FAST &amp; AFFORDABLE SERVICE</div>
  </div>

  <svg class="equipment" viewBox="0 0 430 445" role="img" aria-label="Technician in overalls standing beside solar panels, outdoor AC condenser, mini-split units and a furnace">
    <defs>
      <linearGradient id="equipTone" x1="0" y1="0" x2="0" y2="1">
        <stop offset="0" stop-color="#b4c8ee" stop-opacity="0"/>
        <stop offset="0.35" stop-color="#8e9fbd" stop-opacity="0.55"/>
        <stop offset="1" stop-color="#5d6a80" stop-opacity="0.65"/>
      </linearGradient>
    </defs>
    <rect x="0" y="140" width="430" height="305" rx="10" fill="url(#equipTone)"/>
    <rect x="220" y="0" width="180" height="300" rx="10" fill="url(#equipTone)"/>
  </svg>

  <p class="credentials">Licensed<br>&amp;<br>Insured</p>
</main>
</body>
</html>
```